Veterinary Hospital Business Card

We have recently updated our logo and wish to have a business card designed incorporating the new look and flow. We are a full service veterinary hospital also offering laser therapy, boarding, and grooming. Our website is www.thornbrookvets.com

Industry/Entity Type

Veterinary

```html
<!DOCTYPE html>
<html lang="en">
<head>
<meta charset="utf-8">
<title>Thornbrook Animal Hospital – Business Card</title>
<link href="https://fonts.googleapis.com/css2?family=Exo+2:wght@300;400;600&display=swap" rel="stylesheet">
<style>
  :root {
    --bg: #e9ebee;
    --card: #ffffff;
    --brand-blue: #3f7a9e;
    --brand-light: #6ea6c6;
    --ink: #2f3437;
    --ink-soft: #4a5055;
  }
  * { box-sizing: border-box; margin: 0; padding: 0; }
  html, body {
    width: 1200px; height: 892px; overflow: hidden;
    background: var(--bg);
    font-family: "Exo 2", sans-serif;
  }
  .stage {
    position: relative; width: 1200px; height: 892px;
    display: flex; flex-direction: column; align-items: center; justify-content: center; gap: 44px;
  }
  .card {
    position: relative; width: 630px; height: 360px;
    background: var(--card);
    box-shadow: 0 6px 22px rgba(0,0,0,0.12);
    overflow: hidden;
  }
  .card__band { position: absolute; inset: 0; width: 100%; height: 100%; }

  /* Front */
  .contact {
    position: absolute; left: 46px; top: 62px;
    color: var(--ink);
  }
  .contact__name {
    font-size: 22px; font-weight: 400; letter-spacing: 1px;
    color: var(--brand-blue); text-transform: uppercase;
  }
  .contact__title {
    font-size: 14px; font-weight: 400; letter-spacing: 1.2px;
    color: var(--ink-soft); text-transform: uppercase; margin-top: 2px;
  }
  .contact__address {
    font-size: 15px; line-height: 20px; margin-top: 30px; letter-spacing: 0.5px;
  }
  .contact__list { list-style: none; margin-top: 24px; }
  .contact__item {
    display: flex; align-items: center; gap: 10px;
    font-size: 13px; line-height: 22px; letter-spacing: 0.4px;
  }
  .contact__icon { width: 13px; height: 13px; fill: var(--ink-soft); flex: none; }

  .brand {
    position: absolute; right: 44px; top: 70px;
    display: flex; align-items: center; gap: 12px;
  }
  .brand__dot {
    width: 22px; height: 22px; border-radius: 50%; background: var(--brand-blue);
  }
  .brand__name {
    font-size: 26px; font-weight: 600; line-height: 30px;
    color: var(--brand-blue); text-transform: uppercase; letter-spacing: 1px;
  }
</style>
</head>
<body>
<main class="stage">

  <section class="card card--front" aria-label="Business card front">
    <svg class="card__band" viewBox="0 0 630 360" aria-hidden="true">
      <polygon points="500,360 630,255 630,360" fill="var(--brand-blue)"/>
    </svg>

    <div class="brand">
      <span class="brand__dot"></span>
      <span class="brand__name">Thornbrook<br>Animal Hospital</span>
    </div>

    <div class="contact">
      <h1 class="contact__name">Daniel Reyes</h1>
      <p class="contact__title">General Manager</p>
      <p class="contact__address">42 Alder Vale Road,<br>2nd floor, Suite B.</p>
      <ul class="contact__list">
        <li class="contact__item">
          <svg class="contact__icon" viewBox="0 0 16 16"><path d="M3.6 1.2l2.3 2.6-1.3 1.8c.9 2 2.5 3.6 4.5 4.5l1.8-1.3 2.6 2.3-1.3 2.3C7.3 15.1 1 8.7 1.3 2.5z"/></svg>
          <span>012 555 0147</span>
        </li>
        <li class="contact__item">
          <svg class="contact__icon" viewBox="0 0 16 16"><path d="M4 1h8v14H4zM5.5 2.5v9h5v-9zM7 12.8h2v1H7z" fill-rule="evenodd"/></svg>
          <span>012 555 0148</span>
        </li>
        <li class="contact__item">
          <svg class="contact__icon" viewBox="0 0 16 16"><path d="M1 3h14v10H1zM2 4l6 5 6-5v1L8 10 2 5z" fill-rule="evenodd"/></svg>
          <span>hello@thornbrookvets.com</span>
        </li>
        <li class="contact__item">
          <svg class="contact__icon" viewBox="0 0 16 16"><circle cx="8" cy="8" r="7"/><path d="M1 8h14M8 1c-3 3-3 11 0 14M8 1c3 3 3 11 0 14" stroke="#fff" stroke-width="1" fill="none"/></svg>
          <span>www.thornbrookvets.com</span>
        </li>
      </ul>
    </div>
  </section>

  <section class="card card--back" aria-label="Business card back">
    <svg class="card__band" viewBox="0 0 630 360" aria-hidden="true">
      <polygon points="0,0 130,0 0,105" fill="var(--brand-blue)"/>
      <polygon points="500,360 630,255 630,360" fill="var(--brand-blue)"/>
    </svg>
  </section>

</main>
</body>
</html>
```